Combining 2 Websites into 1 Website

Hi, we are merging our 2 business websites into 1 website. A little bit our business. We are a Wholesale Food Company (Kandel Vita PNG Ltd) with a number of retail businesses including a Deli Butchery/Bakery (named The Rowly Grill Hof) and Fast Food Restaurants (Condor Stack, Tok Tam Rol, Gulpers) and a catering company called Rowly Dano Catering. At our head office (Kandel Vita) we also have 2 manufacturing factories - Bakery (Rowly Crust Hof products) and Butchery (Rowly Fine products).
Our current websites are:
- www.kandelvitapng.example (mother company)
- www.grillhof.example
We are looking to put all our brands under one website, with url www.kvz.example . The new website will contain the following pages:
www.kvz.example (home page)
About Us (similar look to our Kandel Vita Company Profile attached)
Contact (for Kandel Vita head office/sales)
All retail brand logos (click on a logo and be taken to that brands page)
www.kvz.example/grillhof
o Location
o Contact
o Order Online
www.kvz.example/condorstack
o Locations
o Contacts
o Order Online
www.kvz.example/toktamrol
o Location
o Contact
www.kvz.example/gulpers
o Location
o Contact
o Order Online
www.kvz.example/rowlydanocatering
o Location
o Contact
www.kvz.example/careers
o Information on how to apply for a job
o E-form that applicants complete and upload any paperwork to be sent to us? Name, DOB, Current Address, Phone Number, upload SV and Cover Letter
www.kvz.example/shoponline
All online retails will link to this page to do an online orders (like we have setup on our Grill Hof page). Only complexity is that Delivery Charge will need to be seperate for Grill Hof products vs Condor Stack / Gulpers products.
Information for the Kandel Vita home page can be found on the attached company Profile. Information (contact, location ect) can be found on our existing Grill Hof web page).
I have attached each of our logos. I have also attached a tribal fish design (pdf) which we use on all business cards, email signatures and uniforms across all sites. Logos include (all .png files):
- Kandel Vita Logo
- Grill Hof Logo
- Condor Stack Logo
- Gulpers Logo
- Tok Tam Rol Logo
- Rowly Dano Catering Logo
- Crust Hof Logo (for Kandel Vita - Bakery Factory Products)
- Rowly Fine logo (for Kandel Vita - Butchery Factory Products)
- QLSTM logo (Quality Assurance cert of our Butchery Factory)
Modern, Fun, Corporate
Food - Manufacturing, Wholesale & Delivery, Retail, Restaurants, Catering
Coded - Design and coding required
5+ page

```html
<!DOCTYPE html>
<html lang="en">
<head>
<meta charset="utf-8">
<title>Kandel Vita PNG Ltd</title>
<link href="https://fonts.googleapis.com/css2?family=Tinos:wght@400;700&family=Lato:wght@400;700&display=swap" rel="stylesheet">
<style>
:root{
  --red:#e3121c;
  --red-deep:#c70f18;
  --ink:#111111;
  --text:#333333;
  --muted:#f2f3f5;
  --white:#ffffff;
  --line:#bdbdbd;
}
*{box-sizing:border-box;margin:0;padding:0}
html,body{width:1200px;height:4261px;overflow:hidden}
body{font-family:"Lato",sans-serif;color:var(--text);background:var(--white);position:relative}
.abs{position:absolute}
.btn{position:absolute;background:var(--red);color:var(--white);font-family:"Tinos",serif;font-weight:700;font-size:15px;border-radius:26px;display:flex;align-items:center;justify-content:center}
.accent{color:var(--red)}
.underline-mark{position:absolute;height:4px;background:var(--red);border-radius:2px}

/* header */
.site-header{position:absolute;left:0;top:0;width:1200px;height:103px;background:var(--white);z-index:3}
.top-contact{position:absolute;top:20px;font-size:12.5px;color:var(--ink);display:flex;align-items:center;gap:8px}
.top-rule{position:absolute;top:54px;height:1px;background:var(--line)}
.main-nav{position:absolute;top:67px;font-size:11.5px;font-weight:700;color:var(--ink);display:flex;gap:34px;text-transform:uppercase}
.main-nav .active{color:var(--red)}
.brand-badge{position:absolute;left:494px;top:4px;width:224px;height:118px;border-radius:50%;background:var(--white);border:5px solid var(--red);display:flex;align-items:center;justify-content:center;z-index:4}
.brand-badge span{font-family:"Tinos",serif;font-weight:700;font-size:30px;color:var(--ink)}
.icon-box{position:absolute;top:8px;width:36px;height:36px;border:2px solid var(--red);border-radius:5px;display:flex;align-items:center;justify-content:center}
.cart-label{position:absolute;left:1048px;top:6px;font-size:11px;font-weight:700;color:var(--ink)}
.cart-total{position:absolute;left:1048px;top:16px;font-family:"Tinos",serif;font-weight:700;font-size:27px;color:var(--red)}

/* hero */
.hero{position:absolute;left:0;top:103px;width:1200px;height:640px;overflow:hidden}
.hero-photo{position:absolute;inset:0;background:
  radial-gradient(ellipse 620px 200px at 560px 250px,rgba(150,40,55,.55) 0%,rgba(120,70,40,.35) 55%,rgba(0,0,0,0) 100%),
  linear-gradient(180deg,#2e2e2e 0%,#232323 55%,#181818 100%)}
.hero-title{position:absolute;left:0;width:1200px;top:152px;text-align:center;font-family:"Tinos",serif;font-weight:700;font-size:100px;color:var(--white);letter-spacing:1px;line-height:1}
.hero-sub{position:absolute;left:0;width:1200px;top:260px;text-align:center;font-family:"Tinos",serif;font-weight:700;font-size:30px;color:var(--white)}
.hero-text{position:absolute;left:200px;width:800px;top:328px;text-align:center;font-size:12.5px;line-height:28px;color:var(--white)}
.hero-arrow{position:absolute;top:290px}

/* about */
.about-title{position:absolute;left:120px;top:852px;font-family:"Tinos",serif;font-weight:700;font-size:40px;color:var(--ink)}
.about-copy{position:absolute;left:120px;top:927px;width:466px;font-size:13.5px;line-height:28px;text-align:justify;color:var(--text)}
.about-copy p+p{margin-top:28px}
.about-ring{position:absolute;left:627px;top:818px;width:458px;height:458px;border-radius:50%;border:5px solid var(--red);background:var(--white)}
.about-photo{position:absolute;left:643px;top:834px;width:426px;height:426px;border-radius:50%;background:
  radial-gradient(ellipse 170px 150px at 50% 56%,rgba(200,140,70,.9) 0%,rgba(160,90,45,.6) 55%,rgba(0,0,0,0) 100%),
  linear-gradient(180deg,#3a3a3e 0%,#2a2a2d 100%)}

/* why choose */
.why{position:absolute;left:0;top:1395px;width:1200px;height:937px;background:var(--muted)}
.section-title{position:absolute;left:0;width:1200px;text-align:center;font-family:"Tinos",serif;font-weight:700;font-size:38px;color:var(--ink)}
.feature{position:absolute;width:300px;text-align:center}
.feature-icon{display:block;margin:0 auto;width:160px;height:150px}
.feature h3{margin-top:12px;font-family:"Tinos",serif;font-weight:700;font-size:19px;color:var(--ink)}
.feature h3.accent{color:var(--red)}
.feature p{margin:4px auto 0;width:280px;font-size:13px;line-height:28px;color:var(--text)}

/* retail brands */
.brands{position:absolute;left:0;top:2332px;width:1200px;height:740px;background:linear-gradient(180deg,#d91822 0%,#e11a24 50%,#c8121b 100%)}
.brands .section-title{color:var(--white)}
.brand-card{position:absolute;top:176px;width:170px;height:90px;background:var(--white);border-radius:8px;display:flex;align-items:center;justify-content:center;text-align:center;font-family:"Tinos",serif;font-weight:700;font-size:16px;color:var(--red);padding:0 10px}
.brand-card.ink{color:var(--ink)}
.cert-shape{width:90px;height:40px;border-radius:6px;background:#222}
.brand-panel{position:absolute;left:152px;top:300px;width:894px;height:356px;background:var(--white);border-radius:14px;text-align:center}
.panel-name{position:absolute;left:0;width:894px;top:44px;font-family:"Tinos",serif;font-weight:700;font-size:34px;color:var(--ink)}
.panel-address{position:absolute;left:0;width:894px;top:114px;display:flex;justify-content:center;align-items:center;gap:10px;font-family:"Tinos",serif;font-weight:700;font-size:14px;color:var(--ink)}
.pin-dot{width:34px;height:34px;border-radius:50%;background:var(--red);display:flex;align-items:center;justify-content:center}
.panel-text{position:absolute;left:37px;width:820px;top:156px;font-size:13.5px;line-height:28px;color:var(--text)}

/* apply */
.apply-sub{position:absolute;left:0;width:1200px;top:3238px;text-align:center;font-size:14px;color:var(--ink)}
.field{position:absolute;height:52px;border:1px solid #9a9a9a;font-size:13.5px;color:#444;padding:0 14px;display:flex;align-items:center;background:var(--white)}
.field.area{align-items:flex-start;padding-top:16px;gap:6px}

/* footer */
.footer{position:absolute;left:0;top:3690px;width:1200px;height:571px}
.footer-badge{position:absolute;left:488px;top:192px;width:224px;height:118px;border-radius:50%;border:5px solid var(--red);display:flex;align-items:center;justify-content:center}
.footer-badge span{font-family:"Tinos",serif;font-weight:700;font-size:30px;color:var(--white)}
.footer-nav{position:absolute;left:0;width:1200px;top:333px;display:flex;justify-content:center;gap:34px;font-size:12px;font-weight:700;color:var(--white);text-transform:uppercase}
.footer-rule{position:absolute;left:128px;width:944px;height:1px;background:#6b6b6b}
.footer-contacts{position:absolute;left:0;width:1200px;top:397px;display:flex;justify-content:center;gap:48px;font-size:11.5px;color:var(--white)}
.footer-contacts span{display:flex;align-items:center;gap:8px}
.copyright{position:absolute;left:0;width:1200px;top:480px;text-align:center;font-size:11.5px;color:var(--white)}
.socials{position:absolute;left:524px;top:513px;display:flex;gap:8px}
.socials i{display:block;width:32px;height:32px;border-radius:50%;border:1.5px solid var(--white)}
</style>
</head>
<body>

<header class="site-header">
  <div class="top-contact" style="left:84px">
    <svg width="12" height="12" viewBox="0 0 24 24"><path fill="#e3121c" d="M6.6 10.8a15 15 0 0 0 6.6 6.6l2.2-2.2c.3-.3.7-.4 1-.2 1.1.4 2.3.6 3.6.6.6 0 1 .4 1 1V20c0 .6-.4 1-1 1A17 17 0 0 1 3 4c0-.6.4-1 1-1h3.5c.6 0 1 .4 1 1 0 1.3.2 2.5.6 3.6.1.3 0 .7-.2 1z"/></svg>
    (+675) 7000 1234
  </div>
  <div class="top-contact" style="left:256px">
    <svg width="13" height="11" viewBox="0 0 24 18"><rect width="24" height="18" rx="2" fill="#e3121c"/><path d="M2 2l10 8 10-8" stroke="#fff" stroke-width="2" fill="none"/></svg>
    sales@kandelvitapng.example
  </div>
  <div class="top-rule" style="left:80px;width:380px"></div>
  <div class="top-rule" style="left:740px;width:380px"></div>
  <nav class="main-nav" style="left:96px">
    <span class="active">Home</span><span>About Us</span><span>All Retail Brand</span>
  </nav>
  <nav class="main-nav" style="left:760px">
    <span>How to Apply</span><span>Testimonials</span><span>Contact Us</span>
  </nav>

  <div class="icon-box" style="left:904px">
    <svg width="16" height="16" viewBox="0 0 24 24"><circle cx="12" cy="7" r="5" fill="#e3121c"/><path d="M2 23c0-6 4-9 10-9s10 3 10 9z" fill="#e3121c"/></svg>
  </div>
  <div class="icon-box" style="left:950px">
    <svg width="16" height="16" viewBox="0 0 24 24"><circle cx="10" cy="10" r="7" stroke="#e3121c" stroke-width="3" fill="none"/><path d="M15 15l7 7" stroke="#e3121c" stroke-width="3"/></svg>
  </div>
  <div class="icon-box" style="left:996px">
    <svg width="18" height="16" viewBox="0 0 26 22"><path d="M1 2h4l3 12h13l3-9H7" stroke="#e3121c" stroke-width="2.5" fill="#e3121c"/><circle cx="10" cy="19" r="2" fill="#e3121c"/><circle cx="19" cy="19" r="2" fill="#e3121c"/></svg>
  </div>
  <div class="cart-label">MY CART</div>
  <div class="cart-total">00.00</div>
</header>
<div class="brand-badge"><span>Kandel Vita</span></div>

<section class="hero">
  <div class="hero-photo" role="img" aria-label="Raw steaks with rosemary on a wooden board over a dark wood table"></div>
  <div class="hero-title">Kandel Vita</div>
  <div class="hero-sub">PNG LTD</div>
  <p class="hero-text">Our mission is to procure a great variety of high quality chilled and frozen food products at the most affordable prices, to supply small and large wholesale, retail, restaurant and catering businesses throughout Papua New Guinea.</p>
  <div class="btn" style="left:520px;top:397px;width:160px;height:48px">Order Online</div>
  <svg class="hero-arrow" style="left:48px" width="22" height="44" viewBox="0 0 22 44"><path d="M20 2L2 22l18 20" stroke="#fff" stroke-width="2" fill="none"/></svg>
  <svg class="hero-arrow" style="left:1132px" width="22" height="44" viewBox="0 0 22 44"><path d="M2 2l18 20L2 42" stroke="#fff" stroke-width="2" fill="none"/></svg>
  <svg class="abs" style="left:0;top:520px" width="1200" height="120" viewBox="0 0 1200 120" preserveAspectRatio="none">
    <path d="M0 60 C250 130 520 110 760 70 S1080 10 1200 40 L1200 120 L0 120Z" fill="#e3121c"/>
    <path d="M0 72 C250 140 520 120 760 80 S1080 22 1200 52 L1200 120 L0 120Z" fill="#fff"/>
  </svg>
</section>

<h2 class="about-title">About <span class="accent">Kandel Vita PNG</span></h2>
<div class="underline-mark" style="left:120px;top:905px;width:88px"></div>
<div class="about-copy">
  <p>Kandel Vita PNG has been operating since 2011. Although the company is fairly new, it is run under the direction of company owners Rolf and Mera Tandy who have lived and worked in PNG for more than 30 years, with experience in the highlands, the islands and central PNG.</p>
  <p>Our mission is to procure a great variety of high quality chilled and frozen food products at the most affordable prices, to supply small and large wholesale, retail, restaurant and catering businesses throughout Papua New Guinea. We currently supply both rural and local customers based in Rabaul, Kieta, Tabubil, Alotau and Port Moresby.</p>
</div>
<div class="btn" style="left:120px;top:1222px;width:161px;height:52px">Learn More</div>
<div class="about-ring"></div>
<div class="about-photo" role="img" aria-label="Cheeseburger with lettuce, tomato and onion on a sesame bun"></div>

<section class="why">
  <h2 class="section-title" style="top:72px">Why <span class="accent">Choose Us</span></h2>
  <div class="underline-mark" style="left:562px;top:125px;width:76px"></div>

  <div class="feature" style="left:121px;top:190px">
    <svg class="feature-icon" viewBox="0 0 160 150" aria-hidden="true">
      <g fill="none" stroke="#e3121c" stroke-width="2.5">
        <circle cx="80" cy="48" r="9"/><path d="M66 78c0-12 6-18 14-18s14 6 14 18"/>
        <path d="M58 82l3 7 7 1-5 5 1 7-6-3-6 3 1-7-5-5 7-1z"/>
        <path d="M80 82l3 7 7 1-5 5 1 7-6-3-6 3 1-7-5-5 7-1z"/>
        <path d="M102 82l3 7 7 1-5 5 1 7-6-3-6 3 1-7-5-5 7-1z"/>
      </g>
      <rect x="16" y="120" width="144" height="5" fill="#111"/>
    </svg>
    <h3>Experience</h3>
    <p>Kandel Vita currently supply food products to a large number of companies located in both urban and rural locations across PNG. Management are highly experienced.</p>
  </div>
  <div class="feature" style="left:451px;top:190px">
    <svg class="feature-icon" viewBox="0 0 160 150" aria-hidden="true">
      <g fill="none" stroke="#e3121c" stroke-width="2.5">
        <rect x="54" y="38" width="52" height="68" rx="4"/>
        <path d="M54 58h52M54 82h52"/>
        <path d="M64 48h10M64 70h32M64 94h32"/>
      </g>
      <rect x="16" y="120" width="144" height="5" fill="#e3121c"/>
    </svg>
    <h3 class="accent">Storage and Infrastructure</h3>
    <p>Kandel Vita hold 25 transportable refrigerated 20ft containers that can store frozen and chilled product at any location across PNG with power.</p>
  </div>
  <div class="feature" style="left:782px;top:190px">
    <svg class="feature-icon" viewBox="0 0 160 150" aria-hidden="true">
      <g fill="none" stroke="#e3121c" stroke-width="2.5">
        <rect x="44" y="50" width="52" height="40"/>
        <path d="M96 62h16l10 14v14H96z"/>
        <circle cx="62" cy="96" r="6" fill="#fff"/><circle cx="110" cy="96" r="6" fill="#fff"/>
      </g>
      <rect x="16" y="120" width="144" height="5" fill="#111"/>
    </svg>
    <h3>Transport</h3>
    <p>Kandel Vita have a fleet of different sized temperature-controlled trucks that can deliver products under safe conditions. Our qualified drivers are responsible.</p>
  </div>

  <div class="feature" style="left:121px;top:550px">
    <svg class="feature-icon" viewBox="0 0 160 150" aria-hidden="true">
      <g fill="none" stroke="#e3121c" stroke-width="2.5">
        <circle cx="80" cy="72" r="30"/>
        <path d="M80 86l-14-14a8 8 0 0 1 14-9 8 8 0 0 1 14 9z"/>
      </g>
      <rect x="16" y="120" width="144" height="5" fill="#111"/>
    </svg>
    <h3>Health and Safety</h3>
    <p>Directors Rolf and Mera, administer that food safety and staff safety is of paramount importance. All staff are properly suited, including freezer wear and back .</p>
  </div>
  <div class="feature" style="left:451px;top:550px">
    <svg class="feature-icon" viewBox="0 0 160 150" aria-hidden="true">
      <g fill="none" stroke="#e3121c" stroke-width="2.5">
        <rect x="66" y="40" width="28" height="22"/>
        <path d="M80 40v22"/>
        <path d="M50 74l14 14h32l14-14"/>
        <path d="M64 88l10 12h12l10-12"/>
      </g>
      <rect x="16" y="120" width="144" height="5" fill="#111"/>
    </svg>
    <h3>Suppliers</h3>
    <p>The directors have relationships with top suppliers, abbotoirs, packers and shippers. This ensures competitive pricing, quality and variety of the products.</p>
  </div>
  <div class="feature" style="left:782px;top:550px">
    <svg class="feature-icon" viewBox="0 0 160 150" aria-hidden="true">
      <g fill="none" stroke="#e3121c" stroke-width="2.5">
        <circle cx="58" cy="56" r="9"/><circle cx="80" cy="50" r="11"/><circle cx="102" cy="56" r="9"/>
        <path d="M42 96c0-14 7-22 16-22"/><path d="M118 96c0-14-7-22-16-22"/>
        <path d="M60 100c0-18 9-28 20-28s20 10 20 28z"/>
      </g>
      <rect x="16" y="120" width="144" height="5" fill="#111"/>
    </svg>
    <h3>People</h3>
    <p>We treat our people right, so our people treat you right. The Kandel Vita team is a dedicated hard working bunch and our customer service skills are highly regarded .</p>
  </div>
</section>

<section class="brands">
  <h2 class="section-title" style="top:72px">All Retail Brand</h2>
  <div class="underline-mark" style="left:562px;top:124px;width:76px;background:#fff"></div>

  <div class="brand-card ink" style="left:146px">Rowly Crust Hof</div>
  <div class="brand-card" style="left:330px">Condor Stack</div>
  <div class="brand-card ink" style="left:515px">Tok Tam Rol</div>
  <div class="brand-card" style="left:700px"><div class="cert-shape" role="img" aria-label="Quality certificate badge"></div></div>
  <div class="brand-card" style="left:884px">Rowly Fine</div>
  <svg class="abs" style="left:588px;top:266px" width="24" height="14" viewBox="0 0 24 14"><path d="M0 0h24L12 14z" fill="#fff"/></svg>

  <div class="brand-panel">
    <div class="panel-name">Tok Tam Rol</div>
    <div class="panel-address">
      <span class="pin-dot"><svg width="14" height="18" viewBox="0 0 14 18"><path d="M7 0a7 7 0 0 0-7 7c0 5 7 11 7 11s7-6 7-11a7 7 0 0 0-7-7z" fill="#fff"/><circle cx="7" cy="7" r="2.5" fill="#e3121c"/></svg></span>
      123 Lorem ipsum dolor sit amet, consectetur
    </div>
    <p class="panel-text">Lorem ipsum dolor sit amet, consectetur adipiscing elit, sed do eiusmod tempor incididunt ut labore et dolore magna aliqua. Quis ipsum suspendisse ultrices gravida. Risus commodo viverra maecenas accumsan lacus vel facilisis. unde omnis iste natus error sit voluptatem accusantium doloremque laudantium, totam rem aperiam, eaque ipsa quae ab illo inventore veritatis et quasi architecto beatae vitae dicta sunt explicabo.</p>
    <div class="btn" style="left:367px;top:284px;width:160px;height:48px">Order Online</div>
  </div>
</section>

<h2 class="section-title" style="top:3160px">How to Apply <span class="accent">for a Job</span></h2>
<div class="underline-mark" style="left:562px;top:3213px;width:76px"></div>
<p class="apply-sub">E-form that applicants complete and upload any paperwork to be sent to us?</p>
<div class="field" style="left:223px;top:3288px;width:373px">Full Name</div>
<div class="field" style="left:606px;top:3288px;width:371px">DOB</div>
<div class="field" style="left:223px;top:3353px;width:373px">Current Address</div>
<div class="field" style="left:606px;top:3353px;width:371px">Phone Number</div>
<div class="field area" style="left:223px;top:3418px;width:754px;height:115px">
  <svg width="14" height="14" viewBox="0 0 24 24"><path d="M12 2v13M6 10l6 6 6-6" stroke="#222" stroke-width="3" fill="none"/><path d="M2 17v5h20v-5" stroke="#222" stroke-width="3" fill="none"/></svg>
  Upload SV and Cover Letter
</div>
<div class="btn" style="left:520px;top:3559px;width:160px;height:50px">Apply Now</div>

<footer class="footer">
  <svg class="abs" style="left:0;top:0" width="1200" height="571" viewBox="0 0 1200 571" preserveAspectRatio="none">
    <path d="M0 90 C300 20 600 0 860 40 S1120 90 1200 50 L1200 571 L0 571Z" fill="#e3121c"/>
    <path d="M0 102 C300 34 600 14 860 54 S1120 104 1200 64 L1200 571 L0 571Z" fill="#0a0a0a"/>
  </svg>
  <div class="footer-badge"><span>Kandel Vita</span></div>
  <nav class="footer-nav"><span>Home</span><span>About Us</span><span>All Retail Brand</span><span>How to Apply</span><span>Testimonials</span><span>Contact Us</span></nav>
  <div class="footer-rule" style="top:372px"></div>
  <div class="footer-contacts">
    <span><svg width="12" height="12" viewBox="0 0 24 24"><path fill="#fff" d="M6.6 10.8a15 15 0 0 0 6.6 6.6l2.2-2.2c.3-.3.7-.4 1-.2 1.1.4 2.3.6 3.6.6.6 0 1 .4 1 1V20c0 .6-.4 1-1 1A17 17 0 0 1 3 4c0-.6.4-1 1-1h3.5c.6 0 1 .4 1 1 0 1.3.2 2.5.6 3.6.1.3 0 .7-.2 1z"/></svg>Phone : (+675) 7000 1234</span>
    <span><svg width="13" height="11" viewBox="0 0 24 18"><rect width="24" height="18" rx="2" fill="#fff"/><path d="M2 2l10 8 10-8" stroke="#0a0a0a" stroke-width="2" fill="none"/></svg>Email : sales@kandelvitapng.example</span>
    <span><svg width="11" height="14" viewBox="0 0 14 18"><path d="M7 0a7 7 0 0 0-7 7c0 5 7 11 7 11s7-6 7-11a7 7 0 0 0-7-7z" fill="#fff"/><circle cx="7" cy="7" r="2.5" fill="#0a0a0a"/></svg>Sec 22, Lot 8-9 Harbour Road KILA, PNG</span>
  </div>
  <div class="footer-rule" style="top:437px"></div>
  <p class="copyright">© copyrights 2022 <span class="accent">Kandel Vita PNG LTD</span> &nbsp;|&nbsp;&nbsp;&nbsp; All rights reserved.</p>
  <div class="socials"><i></i><i></i><i></i><i></i></div>
</footer>

</body>
</html>
```